BUSINESS CARD MIRELLE CAVANOSI

I need a new business card for my personal business.
I am a Naturopath and Nutritionist working doing private consults in the health and wellness arena.
I would like to see designs that are, clean minimalist but colourful.
I like:
White (clean,fresh, minimalist)
pops of one colour ONLY.Choose a colour to run with and keep it simple.
green
light blue
mustard
Bright yellow
Charcoal
The final design should communicate professionalism but also be in touch with nature.
Key Information to include:
MIRELLE CAVANOSI
ABN 48 217 603 915
RQTLBE 327081
Tel 0487 639 142
NATUROPATH | HERBALIST | NUTRITON CONSULTANT
BHSc (Naturopathic Studies) Grad Dip (Naturopathy)
BACK OF CARD : YOUR NEXT APPOINTMENT ..................................
I already have a logo (picture attached)But I would be more than happy to NOT have this included. I am very Open to cards WITHOUT current logo/ ones that weave the colour of my logo but do not use the logo.
I have included pictures attached to give examples of the styles/colors I enjoy.
Updates
I have added a picture of a mortar and pestle - one just like this would be lovely to include in your entry.
TIA

```html
<!DOCTYPE html>
<html lang="en">
<head>
<meta charset="utf-8">
<title>Mirelle Cavanosi Naturopathy – Business Card</title>
<link href="https://fonts.googleapis.com/css2?family=Advent+Pro:wght@300&family=Michroma&family=Exo+2:wght@500&display=swap" rel="stylesheet">
<style>
  :root {
    --stage: #e6e6e4;
    --card-white: #fbfbfb;
    --card-shade: #e4e4e4;
    --accent: #fbb04b;
    --charcoal: #2c302e;
    --ink: #3a3a3a;
    --ink-soft: #6b6b6b;
    --on-accent: #ffffff;
  }
  * { margin: 0; padding: 0; box-sizing: border-box; }
  html, body { width: 1200px; height: 899px; overflow: hidden; background: var(--stage); }
  .stage { position: relative; width: 1200px; height: 899px; }

  .card {
    position: absolute;
    width: 600px; height: 343px;
    background: radial-gradient(ellipse at 45% 50%, var(--card-white) 0%, var(--card-white) 40%, var(--card-shade) 100%);
    box-shadow: 0 6px 18px rgba(0,0,0,.18);
    overflow: hidden;
  }
  .card--back { left: 80px; top: 70px; }
  .card--front { left: 520px; top: 470px; }

  .brand { display: flex; align-items: center; gap: 12px; }
  .brand__dot { width: 30px; height: 30px; border-radius: 50%; background: var(--accent); flex: none; }
  .brand__name {
    font-family: "Advent Pro", sans-serif; font-weight: 300;
    color: var(--ink-soft); letter-spacing: 2px; line-height: 1.05;
    text-transform: uppercase;
  }
  .card--back .brand { position: absolute; left: 50%; top: 50%; transform: translate(-50%, -50%); flex-direction: column; gap: 10px; text-align: center; }
  .card--back .brand__dot { width: 38px; height: 38px; }
  .card--back .brand__name { font-size: 26px; }

  .card__swoosh { position: absolute; inset: 0; width: 100%; height: 100%; }

  .card--front .brand { position: absolute; left: 28px; top: 118px; }
  .card--front .brand__name { font-size: 22px; }

  .holder { position: absolute; right: 20px; top: 74px; text-align: right; color: var(--on-accent); }
  .holder__name { font-family: "Michroma", sans-serif; font-size: 16px; letter-spacing: 1px; white-space: nowrap; }
  .holder__role { font-family: "Exo 2", sans-serif; font-weight: 500; font-size: 13px; margin-top: 5px; letter-spacing: .5px; }

  .contact { position: absolute; left: 26px; top: 196px; list-style: none; font-family: "Exo 2", sans-serif; font-weight: 500; color: var(--ink); font-size: 12.5px; }
  .contact li { display: flex; align-items: center; gap: 8px; height: 22px; letter-spacing: .8px; }
  .contact svg { width: 12px; height: 12px; fill: var(--ink); flex: none; }

  .address { position: absolute; right: 30px; bottom: 14px; text-align: right; font-family: "Exo 2", sans-serif; font-weight: 500; color: var(--ink); font-size: 14px; line-height: 1.45; letter-spacing: .8px; }
</style>
</head>
<body>
<main class="stage">

  <section class="card card--back" aria-label="Card back">
    <div class="brand">
      <span class="brand__dot"></span>
      <span class="brand__name">Mirelle Cavanosi<br>Naturopathy</span>
    </div>
  </section>

  <section class="card card--front" aria-label="Card front">
    <svg class="card__swoosh" viewBox="0 0 600 343" preserveAspectRatio="none" aria-hidden="true">
      <path d="M0,0 H600 V230 C540,130 340,78 0,76 Z" fill="var(--accent)"/>
      <path d="M0,84 C340,86 545,140 600,240 V300 C540,170 340,94 0,92 Z" fill="var(--charcoal)"/>
    </svg>

    <div class="brand">
      <span class="brand__dot"></span>
      <span class="brand__name">Mirelle Cavanosi<br>Naturopathy</span>
    </div>

    <div class="holder">
      <p class="holder__name">DORIAN VELL</p>
      <p class="holder__role">Managing Director</p>
    </div>

    <ul class="contact">
      <li><svg viewBox="0 0 24 24"><path d="M6.6 10.8a15 15 0 0 0 6.6 6.6l2.2-2.2a1 1 0 0 1 1-.25 11.4 11.4 0 0 0 3.6.57 1 1 0 0 1 1 1V20a1 1 0 0 1-1 1A17 17 0 0 1 3 4a1 1 0 0 1 1-1h3.5a1 1 0 0 1 1 1c0 1.250.2 2.450.57 3.570a1 1 0 0 1-.25 1z"/></svg>024 618 3907</li>
      <li><svg viewBox="0 0 24 24"><path d="M7 1h10a2 2 0 0 1 2 2v18a2 2 0 0 1-2 2H7a2 2 0 0 1-2-2V3a2 2 0 0 1 2-2zm0 3v14h10V4zm5 15.5a1 1 0 1 0 0 2 1 1 0 0 0 0-2z"/></svg>024 618 3907</li>
      <li><svg viewBox="0 0 24 24"><path d="M6 2h9v6H6zM3 9h18v13H3zm4 3v2h2v-2zm4 0v2h2v-2zm4 0v2h2v-2zm-8 4v2h2v-2zm4 0v2h2v-2z"/></svg>024 618 3907</li>
      <li><svg viewBox="0 0 24 24"><path d="M2 5h20v14H2zm2 2v.5l8 5 8-5V7l-8 5z"/></svg>mail@verdantleaf.com</li>
      <li><svg viewBox="0 0 24 24"><path d="M12 2a10 10 0 1 0 0 20 10 10 0 0 0 0-20zm6.9 9h-3a15 15 0 0 0-1.3-5.6A8 8 0 0 1 18.9 11zM12 4.1c.9 1.2 1.8 3.6 1.9 6.9h-3.8c.1-3.3 1-5.7 1.9-6.9zM9.4 5.4A15 15 0 0 0 8.1 11h-3a8 8 0 0 1 4.3-5.6zM5.1 13h3a15 15 0 0 0 1.3 5.6A8 8 0 0 1 5.1 13zm6.9 6.9c-.9-1.2-1.8-3.6-1.9-6.9h3.8c-.1 3.3-1 5.7-1.9 6.9zm2.6-1.3a15 15 0 0 0 1.3-5.6h3a8 8 0 0 1-4.3 5.6z"/></svg>www.verdantleaf.com</li>
    </ul>

    <p class="address">27 Birchwood Lane<br>Level 4, Ashvale</p>
  </section>

</main>
</body>
</html>
```